Orthopedist website

We need a web design for a relaunch of this website: http://www.gelenkwerk-praxis.example/
This website is for a orthopedist. Please fell free to create a modern and clean layout. The currently used colours need not to be used in the new design.
The website should transport reliability so that patients will call or contact the doctor for a treatment.
A specially logo is not available.
Reason: We will get a new logo which should be integrated into the design.
Reason: Customer will get a new logo (is ready soon).
Target Market(s)
The target market are patients from salzburg / austria which have orthopedic problems (hand, feet, backbone)
Industry/Entity Type
Doctor
Look and feel

```html
<!DOCTYPE html>
<html lang="de">
<head>
<meta charset="utf-8">
<title>Orthopädie Dr.Berger</title>
<link rel="stylesheet" href="https://fonts.googleapis.com/css2?family=Arimo:ital,wght@0,400;0,700;1,400&family=Open+Sans:wght@400;700&family=Questrial&family=Crimson+Text:ital@1&display=swap">
<style>
:root{
  --blue:#0099cc;
  --orange:#ff9900;
  --green:#a8e000;
  --ink:#333;
  --muted:#8a8a8a;
  --line:#e2e2e2;
  --panel:#f4f4f4;
  --white:#fff;
}
*{box-sizing:border-box;margin:0;padding:0}
html,body{width:1200px;height:1076px;overflow:hidden;background:var(--white)}
body{position:relative;font-family:"Arimo",Arial,sans-serif;color:var(--ink)}
.abs{position:absolute}
.brand-name{left:148px;top:30px;font-size:29px;color:var(--ink);letter-spacing:-.2px}
.brand-tagline{left:150px;top:64px;font-family:"Crimson Text",Georgia,serif;font-style:italic;font-size:17px;color:var(--blue);letter-spacing:-.3px}
.header-contact{right:150px;top:16px;text-align:right;font-size:13px;color:var(--muted);line-height:16px}
.header-contact .doc{color:var(--orange);font-weight:700;font-size:13px}
.header-contact .phone{color:var(--orange);font-weight:700;font-size:21px;line-height:24px}
.main-nav{left:150px;top:120px;width:900px;height:42px;border:1px solid var(--line);border-bottom:3px solid var(--blue);display:flex}
.main-nav a{font-size:13.5px;color:#444;text-decoration:none;display:flex;align-items:center;justify-content:center;border-right:1px solid var(--line);height:100%}
.main-nav a:last-child{border-right:0;flex:1}
.main-nav a.active{background:var(--blue);color:var(--white)}
.hero{left:152px;top:181px;width:897px;height:399px;background:linear-gradient(180deg,#7f9fce 0%,#b8c9de 45%,#9bb3bf 58%,#cdb190 70%,#b99670 100%)}
.hero-title{left:180px;top:320px;width:460px;font-family:"Open Sans",sans-serif;font-weight:700;font-size:30px;line-height:34px;color:var(--white);text-shadow:0 1px 3px rgba(0,0,0,.35)}
.hero-text{left:181px;top:409px;width:406px;font-size:13px;line-height:17px;color:var(--white);text-align:justify;text-shadow:0 1px 2px rgba(0,0,0,.4)}
.hero-dots{left:184px;top:542px;display:flex;gap:9px}
.hero-dots span{width:10px;height:10px;border-radius:50%;background:var(--white)}
.hero-dots span.on{background:var(--blue)}
.welcome-title{left:151px;top:611px;font-family:"Questrial",sans-serif;font-size:23px;color:var(--blue);letter-spacing:.2px}
.welcome-sub{left:152px;top:638px;font-style:italic;font-size:13px;color:var(--ink)}
.welcome-body{left:150px;top:670px;width:600px;font-size:13px;line-height:17px;color:var(--muted);text-align:justify}
.welcome-body p+p{margin-top:17px}
.info-box{top:850px;width:281px;height:136px;color:var(--white);padding:11px 16px 0}
.info-box h3{font-family:"Questrial",sans-serif;font-weight:400;font-size:18px;letter-spacing:.4px;margin-bottom:8px}
.hours{left:150px;background:var(--blue)}
.hours .row{display:flex;justify-content:space-between;font-size:13px;height:30px;align-items:center;border-top:1px solid rgba(255,255,255,.3);padding-right:3px}
.hours .row:first-of-type{border-top:0}
.contact{left:469px;background:var(--orange)}
.contact .row{display:flex;align-items:center;gap:8px;font-size:13px;height:30px}
.contact svg{width:11px;height:13px;flex:none}
.booking{left:797px;top:615px;width:253px;height:369px;background:var(--panel)}
.booking h2{height:45px;background:var(--green);color:var(--white);font-family:"Open Sans",sans-serif;font-weight:700;font-size:19px;text-align:center;line-height:47px}
.booking .field{position:absolute;left:14px;width:225px;height:32px;background:var(--white);border:1px solid var(--line);font-size:13px;color:#c4c4c4;padding-left:12px;line-height:30px}
.booking .submit{position:absolute;left:153px;top:321px;width:85px;height:30px;background:var(--blue);color:var(--white);font-weight:700;font-size:13px;text-align:center;line-height:30px;border-radius:2px}
.footer-rule{left:150px;top:1026px;width:900px;border-top:1px dotted #bbb}
.footer-copy{left:151px;top:1042px;font-family:"Open Sans",sans-serif;font-size:12px;color:var(--muted)}
.footer-copy b{font-weight:400;color:var(--blue)}
.footer-links{right:150px;top:1042px;font-family:"Open Sans",sans-serif;font-size:12px;color:var(--muted)}
</style>
</head>
<body>
<header>
  <div class="abs brand-name">Dr.med. Lukas M. Berger</div>
  <div class="abs brand-tagline">Orthopädie &amp; Orthopädische Chirurgie Sportmedizin - Chirotherapie</div>
  <div class="abs header-contact">
    <div class="doc">DR.MED. LUKAS M BERGER</div>
    <div class="phone">+43 662 555 01 20</div>
    <div>Ortho-Zentrum Nord</div>
    <div>Lindenhofstr. 14</div>
    <div>5020 Salzburg</div>
  </div>
  <nav class="abs main-nav">
    <a class="active" style="width:95px">Startseite</a>
    <a style="width:129px">Über die Praxis</a>
    <a style="width:151px">Leistungsspektrum</a>
    <a style="width:119px">Patienteninfo</a>
    <a style="width:90px">Aktuelles</a>
    <a style="width:87px">Kontakt</a>
    <a style="width:127px">Ihr Weg zu uns</a>
    <a>Impressum</a>
  </nav>
</header>

<section>
  <div class="abs hero" role="img" aria-label="Photo: two runners jogging along a sandy beach under a blue sky"></div>
  <h1 class="abs hero-title">HERZLICH WILLKOMMEN BEI ORTHOPÄDIE DR.BERGER</h1>
  <p class="abs hero-text">Lorem ipsum dolor sit amet, consectetur adipiscing elit. Nam quis porttitor libero, ac accumsan felis. Vivamus faucibus sapien ac dapibus rhoncus.</p>
  <div class="abs hero-dots"><span></span><span class="on"></span><span></span></div>
</section>

<main>
  <h2 class="abs welcome-title">HERZLICH WILLKOMMEN BEI ORTHOPÄDIE DR.BERGER</h2>
  <div class="abs welcome-sub">Lorem ipsum dolor sit amet</div>
  <div class="abs welcome-body">
    <p>Mit dieser Internetseite stellen wir Ihnen eine Informationsplattform rund um unsere Arztpraxis bereit. Im Rahmen unserer fachärztlich orthopädischen Tätigkeit bieten wir ein breites Spektrum sowohl "schulmedizinischer" als auch "komplementärmedizinischer" Methoden von der Untersuc-hung über manuelle Therapieformen, diversen Injektionstechniken bis hin zu den aktuellen, auch minimalinvasiven Techniken der modernen orthopädischen Chirurgie an.</p>
    <p>Lernen Sie hier unsere Leistungen und unser Praxis-Team kennen.</p>
  </div>

  <div class="abs info-box hours">
    <h3>OPENING HOURS</h3>
    <div class="row"><span>Monday - Friday</span><span>8.00 - 17.00</span></div>
    <div class="row"><span>Saturday</span><span>9.30 - 17.30</span></div>
    <div class="row"><span>Sunday</span><span style="width:77px">Closed</span></div>
  </div>

  <div class="abs info-box contact">
    <h3>CONTACT US</h3>
    <div class="row"><svg viewBox="0 0 11 13"><path d="M5.5 0A4.5 4.5 0 0 0 1 4.5C1 8 5.5 13 5.5 13S10 8 10 4.5A4.5 4.5 0 0 0 5.5 0Zm0 6.2a1.7 1.7 0 1 1 0-3.4 1.7 1.7 0 0 1 0 3.4Z" fill="#fff"/></svg>Lindenhofstr. 14 5020 Salzburg</div>
    <div class="row"><svg viewBox="0 0 11 13"><path d="M3 1 1.5 2.2C1 4 1.8 8 4.7 11.3L6.4 12l1-1.6-2-1.7-1 .6C3.6 8 3.2 6.3 3.4 4.6l1.1-.3L4.3 1.6Z" fill="#fff"/></svg>+43 662 555 01 20</div>
    <div class="row"><svg viewBox="0 0 11 13"><path d="M3 1 1.5 2.2C1 4 1.8 8 4.7 11.3L6.4 12l1-1.6-2-1.7-1 .6C3.6 8 3.2 6.3 3.4 4.6l1.1-.3L4.3 1.6Z" fill="#fff"/></svg>info@gelenkwerk-praxis.example</div>
  </div>

  <aside class="abs booking">
    <h2>MAKE A BOOKING</h2>
    <div class="field" style="top:71px">Your First Name (required)</div>
    <div class="field" style="top:120px">Your Last Name</div>
    <div class="field" style="top:170px">Your Phone (required)</div>
    <div class="field" style="top:219px">Your Email</div>
    <div class="field" style="top:268px">Date of Appointment</div>
    <div class="submit">SUBMIT</div>
  </aside>
</main>

<footer>
  <div class="abs footer-rule"></div>
  <div class="abs footer-copy">Copyright © 2014 <b>ORTHOPÄDIE DR.BERGER</b>. All right reserved.</div>
  <div class="abs footer-links">Terms &amp; Condition &nbsp;|&nbsp; Privacy Policy</div>
</footer>
</body>
</html>
```